Flyer Design Project

We need a flyer design for a 1 year old domestic cleaning company based in Wiltshire, England. We provide households with high quality, hard working cleaners. We would like to see designs which use blue (the colour on the logo attatched). The final design should communicate a clean, premier and thorough service in a clear and bold way. We would like the flyer to be A5 with a single sided design. We have attached an A5 word document with the words we would like to be used in the design, what we need is for you to give it some life, colour, artwork and a professional touch. We are perfectionsists which we would like to illustrate to our customer through this flyer.
Updates

payment has been guaranteed!

Sorry..... please no pictures of females on the designs. many thanks

Target Market(s)

females with higher than average income, aged 30-50. Have families and work 9-5.

Industry/Entity Type

It Company

Requirements
Must have
• The flyer must include the logo attatched and the words in the A5 document attatched. With RELIABLE CLEANERS preferably the headline. A5 - single sided.
The Flyer must also include our introductory offer.....
First Clean FREE
Allow us to demonstrate our standards

this should be emphasised.

PLEASE NOTE: can this be added to the list of words on the flyer please:

Ironing service - one day turn around
Nice to have
• some pictures - nothing cheesey. Again, pictures should communicate our modern professional approach.

```html
<!DOCTYPE html>
<html lang="en">
<head>
<meta charset="utf-8">
<title>Brookmere Cleaners – Reliable Cleaners</title>
<link href="https://fonts.googleapis.com/css2?family=Arimo:wght@700&family=Source+Sans+3:wght@400;600;700&display=swap" rel="stylesheet">
<style>
  :root {
    --blue-deep: #0a6fbf;
    --blue-mid: #1a8fdc;
    --blue-light: #4fb6ef;
    --ink: #1f1f1f;
    --ink-soft: #474747;
    --panel: #ececec;
    --panel-light: #f4f4f4;
    --rule: #c9c9c9;
    --footer: #2a2a2a;
    --accent-orange: #f39a1c;
    --white: #ffffff;
  }
  * { margin: 0; padding: 0; box-sizing: border-box; }
  html, body { width: 846px; height: 1200px; overflow: hidden; background: #ffffff; }
  .flyer {
    position: relative;
    width: 846px;
    height: 1200px;
    overflow: hidden;
    background: linear-gradient(#f6f6f6, #e2e2e2 60%, #e6e6e6);
    font-family: "Source Sans 3", sans-serif;
    color: var(--ink);
  }
  .hero { position: absolute; left: 0; top: 0; width: 846px; height: 730px; }
  .brand {
    position: absolute; left: 28px; top: 60px;
    display: flex; align-items: center; gap: 10px;
    color: var(--white);
  }
  .brand-mark { width: 24px; height: 24px; background: var(--white); border-radius: 50%; }
  .brand-name { font-weight: 700; font-size: 31px; line-height: 1; }
  .brand-tagline {
    position: absolute; left: 86px; top: 94px;
    color: var(--white); font-weight: 700; font-size: 15px;
  }
  .headline-band {
    position: absolute; left: 31px; top: 151px; width: 815px; height: 100px;
    background: linear-gradient(90deg, var(--blue-deep), var(--blue-mid));
    display: flex; align-items: center; justify-content: center;
  }
  .headline {
    font-family: "Arimo", sans-serif; font-weight: 700;
    font-size: 82px; line-height: 1; color: var(--white); letter-spacing: 0.5px;
  }
  .offer { position: absolute; left: 0; top: 752px; width: 846px; text-align: center; }
  .offer-title { font-weight: 700; font-size: 90px; line-height: 1; color: var(--ink); }
  .offer-free { position: relative; display: inline-block; }
  .offer-free::after {
    content: ""; position: absolute; left: -4px; right: -6px; bottom: -4px; height: 5px;
    background: var(--accent-orange); border-radius: 3px; transform: rotate(-1deg);
  }
  .offer-sub { margin-top: 20px; font-weight: 700; font-size: 33px; line-height: 1.2; color: var(--ink); }
  .offer-ironing { margin-top: 6px; font-weight: 700; font-size: 33px; line-height: 1.2; color: var(--ink-soft); }
  .features {
    position: absolute; left: 0; top: 962px; width: 846px; height: 146px;
    border-top: 2px solid var(--rule);
    background: linear-gradient(var(--panel-light), var(--panel));
    display: flex; flex-direction: column; align-items: center; justify-content: center; gap: 8px;
  }
  .feature-row { display: flex; gap: 20px; list-style: none; }
  .feature { display: flex; align-items: center; gap: 9px; font-size: 28px; color: var(--ink); }
  .tick { width: 20px; height: 18px; }
  .contact-bar {
    position: absolute; left: 0; top: 1108px; width: 846px; height: 92px;
    background: var(--footer); color: var(--white);
    display: flex; align-items: center; justify-content: center; gap: 34px;
    font-size: 29px;
  }
  .contact-item { display: flex; align-items: center; gap: 12px; }
  .contact-divider { width: 4px; height: 36px; background: var(--white); }
  .contact-icon { width: 36px; height: 36px; }
</style>
</head>
<body>
<main class="flyer">
  <svg class="hero" viewBox="0 0 846 730">
    <defs>
      <linearGradient id="roomTone" x1="0.3" y1="0" x2="0.6" y2="1">
        <stop offset="0" stop-color="#f1f3f4"/>
        <stop offset="0.3" stop-color="#d6d9da"/>
        <stop offset="0.55" stop-color="#b3b3b1"/>
        <stop offset="0.8" stop-color="#7c7a78"/>
        <stop offset="1" stop-color="#5b5a59"/>
      </linearGradient>
      <linearGradient id="sideBlue" x1="0" y1="0" x2="1" y2="1">
        <stop offset="0" stop-color="#0a6fbf"/>
        <stop offset="1" stop-color="#2aa0e6"/>
      </linearGradient>
      <linearGradient id="waveBlue" x1="0" y1="0" x2="1" y2="0">
        <stop offset="0" stop-color="#0a6fbf"/>
        <stop offset="0.6" stop-color="#1a8fdc"/>
        <stop offset="1" stop-color="#4fb6ef"/>
      </linearGradient>
    </defs>
    <rect width="846" height="730" fill="#e6e6e6"/>
    <path role="img" aria-label="Photo of a bright modern living room with a grey sofa, a rug and a blue bucket of cleaning products"
          d="M0 0 H846 V640 C640 690 360 700 0 690 Z" fill="url(#roomTone)"/>
    <path d="M0 0 H470 C400 40 320 90 290 150 L230 252 C140 300 76 380 70 470 C66 560 84 615 130 660 L0 660 Z"
          fill="url(#sideBlue)"/>
    <path d="M230 252 C140 300 76 380 70 470 C66 560 84 615 130 660"
          fill="none" stroke="#ffffff" stroke-width="4"/>
    <path d="M0 640 C250 700 560 690 846 620 V650 C600 715 300 725 0 690 Z" fill="url(#waveBlue)"/>
    <path d="M0 690 C300 725 600 715 846 650 V662 C600 730 300 735 0 702 Z" fill="#9fd6f5"/>
  </svg>

  <div class="brand">
    <span class="brand-mark"></span>
    <span class="brand-name">Brookmere Cleaners</span>
  </div>
  <p class="brand-tagline">Premier Domestic Cleaners</p>

  <div class="headline-band">
    <h1 class="headline">Reliable Cleaners!</h1>
  </div>

  <section class="offer">
    <h2 class="offer-title">First Clean <span class="offer-free">FREE</span></h2>
    <p class="offer-sub">Allow us to demonstrate our standards</p>
    <p class="offer-ironing">Ironing service - One day turn around</p>
  </section>

  <section class="features">
    <ul class="feature-row">
      <li class="feature"><svg class="tick" viewBox="0 0 20 18"><path d="M2 9 L8 15 L18 2" fill="none" stroke="#1a8fdc" stroke-width="3.5" stroke-linecap="round"/></svg>Personalised service</li>
      <li class="feature"><svg class="tick" viewBox="0 0 20 18"><path d="M2 9 L8 15 L18 2" fill="none" stroke="#1a8fdc" stroke-width="3.5" stroke-linecap="round"/></svg>Constantly thorough</li>
      <li class="feature"><svg class="tick" viewBox="0 0 20 18"><path d="M2 9 L8 15 L18 2" fill="none" stroke="#1a8fdc" stroke-width="3.5" stroke-linecap="round"/></svg>Hassel free</li>
    </ul>
    <ul class="feature-row">
      <li class="feature"><svg class="tick" viewBox="0 0 20 18"><path d="M2 9 L8 15 L18 2" fill="none" stroke="#1a8fdc" stroke-width="3.5" stroke-linecap="round"/></svg>Insured</li>
      <li class="feature"><svg class="tick" viewBox="0 0 20 18"><path d="M2 9 L8 15 L18 2" fill="none" stroke="#1a8fdc" stroke-width="3.5" stroke-linecap="round"/></svg>Regular weekly cleans</li>
      <li class="feature"><svg class="tick" viewBox="0 0 20 18"><path d="M2 9 L8 15 L18 2" fill="none" stroke="#1a8fdc" stroke-width="3.5" stroke-linecap="round"/></svg>No contracts</li>
    </ul>
  </section>

  <footer class="contact-bar">
    <span class="contact-item">
      <svg class="contact-icon" viewBox="0 0 24 24"><path d="M6.6 10.8c1.4 2.8 3.8 5.1 6.6 6.6l2.2-2.2c.3-.3.7-.4 1-.2 1.1.4 2.3.6 3.6.6.6 0 1 .4 1 1V20c0 .6-.4 1-1 1C10.6 21 3 13.4 3 4c0-.6.4-1 1-1h3.5c.6 0 1 .4 1 1 0 1.3.2 2.5.6 3.6.1.3 0 .7-.2 1L6.6 10.8z" fill="#ffffff"/></svg>
      07700900417
    </span>
    <span class="contact-divider"></span>
    <span class="contact-item">
      <svg class="contact-icon" viewBox="0 0 36 28"><rect x="2" y="2" width="32" height="24" fill="none" stroke="#ffffff" stroke-width="2.5"/><path d="M2 2 L18 16 L34 2 M2 26 L14 13 M34 26 L22 13" fill="none" stroke="#ffffff" stroke-width="2.5"/></svg>
      brookmerecleaners@mailbox.co.uk
    </span>
  </footer>
</main>
</body>
</html>
```